we need a business card in yellow, green and black with rounded edges. We are in the Construction and Engineering business. I need the below info included:

Neil Barton
Bluestone Engineering & Construction, Inc.
4168 Harbor Crest Road,
Santa Ana, Ca 92814
714-555-0147 Office
714-555-0192 Cell
714-555-0163 Fax
nb@bluestonexq.example

thanks for your help!

```html
<!DOCTYPE html>
<html lang="en">
<head>
<meta charset="utf-8">
<title>Bluestone Engineering &amp; Construction – Business Card</title>
<link rel="stylesheet" href="https://fonts.googleapis.com/css2?family=Source+Sans+3:wght@400;600;700&display=swap">
<style>
  :root {
    --backdrop: #e9e6e0;
    --card-green: #0b8a3e;
    --band-yellow: #f5dc12;
    --divider-white: #ffffff;
    --ink-black: #111111;
    --name-yellow: #f2e11a;
    --title-white: #ffffff;
  }
  * { margin: 0; padding: 0; box-sizing: border-box; }
  html, body {
    width: 1200px; height: 1023px; overflow: hidden;
    background: var(--backdrop);
    font-family: "Source Sans 3", "Myriad Pro", Arial, sans-serif;
  }
  .business-card {
    position: absolute; left: 150px; top: 254px;
    width: 900px; height: 514px;
    border-radius: 34px; overflow: hidden;
    background: var(--card-green);
    box-shadow: 0 10px 28px rgba(0,0,0,0.22);
  }
  .company-band {
    position: absolute; left: 0; top: 0; width: 100%; height: 92px;
    background: var(--band-yellow);
    border-bottom: 5px solid var(--divider-white);
    display: flex; align-items: center; padding-left: 40px;
  }
  .company-name {
    font-size: 40px; font-weight: 600; color: var(--ink-black); letter-spacing: 0.2px;
  }
  .company-name strong { font-weight: 700; }
  .person {
    position: absolute; left: 290px; top: 200px;
    font-size: 40px; line-height: 1;
  }
  .person-name { color: var(--name-yellow); font-weight: 700; }
  .person-sep { color: var(--title-white); font-weight: 400; margin: 0 6px; }
  .person-title { color: var(--title-white); font-weight: 400; }
  .address {
    position: absolute; left: 56px; top: 372px;
    font-size: 25px; line-height: 31px; color: var(--ink-black);
  }
  .contact-list {
    position: absolute; left: 560px; top: 250px; list-style: none;
    font-size: 25px; line-height: 32px; color: var(--ink-black);
  }
  .contact-list li { display: flex; align-items: center; gap: 10px; }
  .contact-icon { width: 18px; height: 18px; flex: none; }
</style>
</head>
<body>
  <section class="business-card">
    <header class="company-band">
      <h1 class="company-name"><strong>Bluestone</strong> Engineering &amp; Construction, Inc.</h1>
    </header>

    <p class="person">
      <span class="person-name">Neil Barton</span><span class="person-sep">|</span><span class="person-title">Owner</span>
    </p>

    <address class="address" style="font-style:normal">
      4168 Harbor Crest Road,<br>
      Santa Ana, Ca 92814
    </address>

    <ul class="contact-list">
      <li>
        <svg class="contact-icon" viewBox="0 0 18 18" aria-label="Office"><path d="M4 2 L7 2 L8 6 L6 7.5 Q8 11 10.5 12 L12 10 L16 11 L16 14 Q15 16 12 16 Q3 14 2 5 Q2 2 4 2 Z" fill="var(--name-yellow)"/></svg>
        714-555-0147
      </li>
      <li>
        <svg class="contact-icon" viewBox="0 0 18 18" aria-label="Cell"><rect x="5" y="1.5" width="8" height="15" rx="1.5" fill="none" stroke="var(--name-yellow)" stroke-width="1.8"/><circle cx="9" cy="13.5" r="1" fill="var(--name-yellow)"/></svg>
        714-555-0192
      </li>
      <li>
        <svg class="contact-icon" viewBox="0 0 18 18" aria-label="Fax"><rect x="5" y="2" width="8" height="5" fill="var(--name-yellow)"/><rect x="2" y="7" width="14" height="8" rx="1.5" fill="var(--name-yellow)"/><rect x="5" y="11" width="8" height="2" fill="var(--card-green)"/></svg>
        714-555-0163
      </li>
      <li>
        <svg class="contact-icon" viewBox="0 0 18 18" aria-label="Email"><rect x="1.5" y="4" width="15" height="11" fill="var(--name-yellow)"/><path d="M2 4.5 L9 10 L16 4.5" fill="none" stroke="var(--ink-black)" stroke-width="1.6"/></svg>
        nb@bluestonexq.example
      </li>
    </ul>
  </section>
</body>
</html>
```